Yard Sign Design Needed

Yard sign needed for mowing & landscaping company. Would like to use the top logo with black background which is attached. Would like MOWING to be in large standout letters. The word "landscaping" can be smaller and more artistic or omitted. Will need room for phone number once design is approved. The phone number will need to stand out and look identical/similar to the word 'MOWING"

```html
<!DOCTYPE html>
<html lang="en">
<head>
<meta charset="utf-8">
<title>Norvale Contractors – Mowing Yard Signs</title>
<link href="https://fonts.googleapis.com/css2?family=Archivo+Black&family=Cinzel:wght@700&display=swap" rel="stylesheet">
<style>
  :root {
    --ink: #05090a;
    --lime: #a6cf45;
    --brand-green: #8aab3a;
    --mist: #f2f2f2;
    --paper: #ffffff;
    --snow: #ffffff;
  }
  * { margin: 0; padding: 0; box-sizing: border-box; }
  html, body {
    width: 1200px; height: 556px; overflow: hidden;
    background: var(--paper);
  }
  .canvas { position: relative; width: 1200px; height: 556px; }

  .sign { position: absolute; overflow: hidden; }
  .sign--landscape { left: 0; top: 70px; width: 556px; height: 417px; }
  .sign--portrait  { left: 783px; top: 0; width: 417px; height: 556px; }

  .panel { position: absolute; }
  .panel--brand  { background: var(--ink); }
  .panel--service { background: var(--lime); }
  .panel--contact { background: var(--mist); }

  .sign--landscape .panel--brand   { left: 0; top: 0; width: 278px; height: 277px; }
  .sign--landscape .panel--service { left: 278px; top: 0; width: 278px; height: 277px; }
  .sign--landscape .panel--contact { left: 0; top: 277px; width: 556px; height: 140px; }

  .sign--portrait .panel--brand   { left: 0; top: 0; width: 417px; height: 278px; }
  .sign--portrait .panel--service { left: 0; top: 278px; width: 417px; height: 138px; }
  .sign--portrait .panel--contact { left: 0; top: 416px; width: 417px; height: 140px; }

  /* company name block */
  .brand-name {
    position: absolute; left: 0; right: 0;
    text-align: center;
    font-family: "Archivo Black", sans-serif;
    color: var(--brand-green);
    line-height: 1;
  }
  .brand-name__main { display: block; }
  .brand-name__sub { display: block; }
  .sign--landscape .brand-name { top: 96px; }
  .sign--landscape .brand-name__main { font-size: 40px; letter-spacing: 1px; }
  .sign--landscape .brand-name__sub { font-size: 19px; letter-spacing: 2px; margin-top: 10px; }
  .sign--portrait .brand-name { top: 100px; }
  .sign--portrait .brand-name__main { font-size: 38px; letter-spacing: 1px; }
  .sign--portrait .brand-name__sub { font-size: 18px; letter-spacing: 2px; margin-top: 10px; }

  /* service headline */
  .service { position: absolute; }
  .service__main {
    display: block;
    font-family: "Archivo Black", sans-serif;
    color: var(--ink);
    line-height: 1;
    white-space: nowrap;
  }
  .service__tag {
    display: block;
    background: var(--ink);
    color: var(--snow);
    font-family: "Cinzel", serif;
    font-weight: 700;
    text-align: center;
    white-space: nowrap;
  }
  .sign--landscape .service { left: 301px; top: 164px; width: 232px; }
  .sign--landscape .service__main { font-size: 48px; letter-spacing: 0.5px; }
  .sign--landscape .service__tag { margin-top: 3px; height: 32px; line-height: 33px; font-size: 24px; letter-spacing: 0.5px; }
  .sign--portrait .service { left: 62px; top: 292px; width: 293px; }
  .sign--portrait .service__main { font-size: 61px; letter-spacing: 0.5px; }
  .sign--portrait .service__tag { margin-top: 1px; height: 40px; line-height: 42px; font-size: 30px; letter-spacing: 1px; }

  /* phone line */
  .phone { position: absolute; display: flex; align-items: center; }
  .phone__badge {
    flex: none; border-radius: 50%;
    background: var(--lime);
    display: flex; align-items: center; justify-content: center;
  }
  .phone__number {
    font-family: "Archivo Black", sans-serif;
    color: var(--ink);
    line-height: 1;
    white-space: nowrap;
  }
  .sign--landscape .phone { left: 20px; top: 305px; }
  .sign--landscape .phone__badge { width: 82px; height: 82px; }
  .sign--landscape .phone__badge svg { width: 50px; height: 50px; }
  .sign--landscape .phone__number { font-size: 62px; margin-left: 18px; }
  .sign--portrait .phone { left: 15px; top: 455px; }
  .sign--portrait .phone__badge { width: 62px; height: 62px; }
  .sign--portrait .phone__badge svg { width: 38px; height: 38px; }
  .sign--portrait .phone__number { font-size: 46px; margin-left: 13px; }
</style>
</head>
<body>
<main class="canvas">

  <section class="sign sign--landscape" aria-label="Landscape yard sign">
    <div class="panel panel--brand">
      <p class="brand-name">
        <span class="brand-name__main">NORVALE</span>
        <span class="brand-name__sub">CONTRACTORS LLC</span>
      </p>
    </div>
    <div class="panel panel--service"></div>
    <div class="panel panel--contact"></div>
    <h2 class="service">
      <span class="service__main">MOWING</span>
      <span class="service__tag">LANDSCAPING</span>
    </h2>
    <p class="phone">
      <span class="phone__badge">
        <svg viewBox="0 0 24 24" aria-hidden="true"><path fill="#05090a" d="M6.6 2.2c.6-.4 1.4-.2 1.8.4l2 3.2c.3.6.2 1.3-.3 1.7L8.6 8.8c1 2.6 3.9 5.6 6.6 6.6l1.3-1.5c.4-.5 1.1-.6 1.7-.3l3.2 2c.6.4.8 1.2.4 1.8l-1.3 2.1c-.6 1-1.8 1.5-3 1.2C10.9 19.3 4.7 13.1 3.3 6.5 3 5.3 3.5 4.1 4.5 3.5z"/></svg>
      </span>
      <span class="phone__number">555-018-472</span>
    </p>
  </section>

  <section class="sign sign--portrait" aria-label="Portrait yard sign">
    <div class="panel panel--brand">
      <p class="brand-name">
        <span class="brand-name__main">NORVALE</span>
        <span class="brand-name__sub">CONTRACTORS LLC</span>
      </p>
    </div>
    <div class="panel panel--service"></div>
    <div class="panel panel--contact"></div>
    <h2 class="service">
      <span class="service__main">MOWING</span>
      <span class="service__tag">LANDSCAPING</span>
    </h2>
    <p class="phone">
      <span class="phone__badge">
        <svg viewBox="0 0 24 24" aria-hidden="true"><path fill="#05090a" d="M6.6 2.2c.6-.4 1.4-.2 1.8.4l2 3.2c.3.6.2 1.3-.3 1.7L8.6 8.8c1 2.6 3.9 5.6 6.6 6.6l1.3-1.5c.4-.5 1.1-.6 1.7-.3l3.2 2c.6.4.8 1.2.4 1.8l-1.3 2.1c-.6 1-1.8 1.5-3 1.2C10.9 19.3 4.7 13.1 3.3 6.5 3 5.3 3.5 4.1 4.5 3.5z"/></svg>
      </span>
      <span class="phone__number">555-018-472</span>
    </p>
  </section>

</main>
</body>
</html>
```